Tirovel

We need a business card for our company is a holding for different business all are different we try to have some air of relax and fun in our projects we add pictures of the office to give you an idea od the mood of the business

Business

```html
<!DOCTYPE html>
<html lang="en">
<head>
<meta charset="utf-8">
<title>Tirovel – Business Card</title>
<link rel="stylesheet" href="https://fonts.googleapis.com/css2?family=Arimo:wght@700&family=Patrick+Hand+SC&display=swap">
<style>
  :root {
    --backdrop: #f3f53e;
    --ink: #1f1f1f;
    --paper: #ffffff;
    --text: #111111;
  }
  * { margin: 0; padding: 0; box-sizing: border-box; }
  html, body {
    width: 1200px;
    height: 1002px;
    overflow: hidden;
    background: var(--backdrop);
  }
  .canvas {
    position: relative;
    width: 1200px;
    height: 1002px;
  }
  .card {
    position: absolute;
    width: 680px;
    height: 400px;
    background: var(--paper);
    overflow: hidden;
  }
  .brand-panel {
    position: absolute;
    left: 300px;
    top: 0;
    width: 380px;
    height: 400px;
    background: var(--ink);
  }

  .contact {
    position: absolute;
    font-family: "Patrick Hand SC", cursive;
    color: var(--text);
    white-space: nowrap;
    line-height: 1;
  }
  .contact-name { left: 38px; top: 70px; font-size: 36px; letter-spacing: 1px; }
  .contact-position { left: 205px; top: 118px; font-size: 19px; }
  .contact-phone { left: 46px; top: 220px; font-size: 26px; letter-spacing: 1px; }
  .contact-email { left: 30px; top: 272px; font-size: 20px; letter-spacing: 0.5px; }

  .wordmark {
    position: absolute;
    left: 320px;
    top: 30px;
    font-family: "Arimo", Arial, sans-serif;
    font-weight: 700;
    color: var(--paper);
    font-size: 118px;
    line-height: 96px;
    letter-spacing: -4px;
  }
  .wordmark span { display: block; }
  .wordmark .wordmark-second { padding-left: 18px; }

  .card-front { left: 492px; top: 300px; }

  .card-back-frame {
    position: absolute;
    left: 60px;
    top: 150px;
    width: 400px;
    height: 680px;
  }
  .card-back {
    left: 0;
    top: 680px;
    transform: rotate(-90deg);
    transform-origin: top left;
  }
</style>
</head>
<body>
<main class="canvas">

  <div class="card-back-frame">
    <section class="card card-back" aria-label="Business card, reverse">
      <div class="brand-panel" role="img" aria-label="Dark brand panel with curved fruit-shaped graphic"></div>
      <p class="contact contact-name">Name Surname</p>
      <p class="contact contact-position">Position</p>
      <p class="contact contact-phone">Phone: 031 45 678</p>
      <p class="contact contact-email">email: hello@tirovel.com</p>
      <h2 class="wordmark"><span>Tiro</span><span class="wordmark-second">vel</span></h2>
    </section>
  </div>

  <section class="card card-front" aria-label="Business card, front">
    <div class="brand-panel" role="img" aria-label="Dark brand panel with curved fruit-shaped graphic"></div>
    <p class="contact contact-name">Name Surname</p>
    <p class="contact contact-position">Position</p>
    <p class="contact contact-phone">Phone: 031 45 678</p>
    <p class="contact contact-email">email: hello@tirovel.com</p>
    <h1 class="wordmark"><span>Tiro</span><span class="wordmark-second">vel</span></h1>
  </section>

</main>
</body>
</html>
```